Business card design for Allied Healthcare provider

We would like a design for front and back of business cards. The design must resonate with all levels of customers from patients, to other health providers and medical. Must also resonate with corporate customers

Target Market(s)

patients, medical practitioners, other health providers and corporate.

Industry/Entity Type

healthcare

Contact Information for Business Card

name, logo, phone and fax numbers, email, website

Requirements
Must have
• not allowing me to change this, but the card must be double sided!! Please take note
Nice to have
• a fresh yet bold design to catch attention.

```html
<!DOCTYPE html>
<html lang="en">
<head>
<meta charset="utf-8">
<title>Brightpath business card</title>
<link rel="stylesheet" href="https://fonts.googleapis.com/css2?family=Roboto:wght@400;500;700&display=swap">
<style>
  :root {
    --navy: #1d2233;
    --orange: #e38a1d;
    --grey: #3b3d44;
    --backdrop: #d9d4cc;
    --card-top: #f6f5f2;
    --card-bottom: #e6e3de;
    --card-edge: #c9c5be;
  }
  * { margin: 0; padding: 0; box-sizing: border-box; }
  html, body { width: 1200px; height: 969px; overflow: hidden; }
  body {
    background: var(--backdrop);
    font-family: "Roboto", sans-serif;
    position: relative;
  }
  .card {
    position: absolute;
    left: 185px; top: 225px;
    width: 868px; height: 494px;
    border-radius: 22px;
    background: linear-gradient(160deg, var(--card-top), var(--card-bottom));
    border: 1px solid var(--card-edge);
    box-shadow: 0 14px 34px rgba(40, 30, 20, 0.18);
  }
  .brand { position: absolute; left: 65px; top: 95px; }
  .brand-name {
    font-size: 42px; font-weight: 500; color: var(--navy);
    letter-spacing: -0.5px; line-height: 1;
  }
  .brand-tagline {
    margin-top: 4px; font-size: 18px; font-weight: 500;
    color: var(--orange); letter-spacing: 0.3px;
  }
  .person { position: absolute; left: 65px; top: 184px; }
  .person-name {
    font-size: 28px; font-weight: 700; color: var(--navy);
    letter-spacing: 0.3px; line-height: 1.1;
  }
  .person-title { font-size: 20px; font-weight: 500; color: var(--orange); margin-top: 3px; }
  .address {
    position: absolute; left: 65px; top: 250px;
    font-size: 19.5px; color: var(--grey); line-height: 24px;
    font-style: normal;
  }
  .contacts { position: absolute; left: 65px; top: 308px; list-style: none; }
  .contacts li {
    display: flex; align-items: center; gap: 10px;
    height: 24.6px; font-size: 19.5px; color: var(--grey);
  }
  .contacts svg { width: 17px; height: 17px; fill: var(--orange); flex: none; }
  .mark {
    position: absolute; left: 500px; top: 210px;
    display: flex; align-items: center; gap: 14px;
  }
  .mark-dot { width: 34px; height: 34px; border-radius: 50%; background: var(--orange); }
  .mark-name {
    font-size: 56px; font-weight: 700; color: var(--navy);
    letter-spacing: -1px; line-height: 1;
  }
</style>
</head>
<body>
  <main class="card">
    <header class="brand">
      <div class="brand-name">brightpath</div>
      <div class="brand-tagline">care • wellness • balance</div>
    </header>

    <section class="person">
      <h1 class="person-name">DANIEL CARTER</h1>
      <div class="person-title">President</div>
    </section>

    <address class="address">
      1420 Willow Crest Road<br>
      Fairbanks, Alaska 99701
    </address>

    <ul class="contacts">
      <li>
        <svg viewBox="0 0 24 24" aria-label="Phone"><path d="M6.6 10.8a15 15 0 0 0 6.6 6.6l2.2-2.2a1 1 0 0 1 1-.25 11.4 11.4 0 0 0 3.6.57 1 1 0 0 1 1 1V20a1 1 0 0 1-1 1A17 17 0 0 1 3 4a1 1 0 0 1 1-1h3.5a1 1 0 0 1 1 1c0 1.25.2 2.45.57 3.57a1 1 0 0 1-.25 1z"/></svg>
        555-204-7731
      </li>
      <li>
        <svg viewBox="0 0 24 24" aria-label="Mobile"><path d="M7 1h10a2 2 0 0 1 2 2v18a2 2 0 0 1-2 2H7a2 2 0 0 1-2-2V3a2 2 0 0 1 2-2zm0 3v14h10V4z"/></svg>
        555-618-3092
      </li>
      <li>
        <svg viewBox="0 0 24 24" aria-label="Fax"><path d="M7 3h10v5H7zM4 9h16a2 2 0 0 1 2 2v7h-4v3H6v-3H2v-7a2 2 0 0 1 2-2zm4 7v3h8v-3z"/></svg>
        555-437-1186
      </li>
      <li>
        <svg viewBox="0 0 24 24" aria-label="Email"><path d="M2 5h20v14H2zm2 2v.5l8 5 8-5V7l-8 5z"/></svg>
        hello@brightpathcare.com
      </li>
      <li>
        <svg viewBox="0 0 24 24" aria-label="Website"><circle cx="12" cy="12" r="10"/></svg>
        brightpathcare.com
      </li>
    </ul>

    <div class="mark">
      <span class="mark-dot"></span>
      <span class="mark-name">brightpath</span>
    </div>
  </main>
</body>
</html>
```